Stylish Business Card for Modern hair salon

I need a simple business card design using our salon logo and colours that are in the logo. We service clients of all ages but predominantly those in the 18 to 55 age range. We have a young staff and are looking to have a card that will present a modern and clean image that represents who we are. The card should be in black and white same as our logo. Minimal use of other colours is allowed.

Industry/Entity Type

Hair And Beauty

Contact Information for Business Card

The design should have the following information
salon name - TR Hair Studio
address - 2751 Birchfield Rd.E. Maplecrest, ON L7P3K2
phone - 555 614-2870
website - trhairexample.ca
instagram - tr.hairstudio
twitter - @TR_HairStudio

Colors
000000
ffffff
474747

Requirements
Must have
• simple design, salon name, address, phone, website, instagram, twitter info
• Back of card should have the following:
• YOUR NEXT APPOINTMENT
• DATE
• TIME
Nice to have
• simple design, clear to see and read,
• predominantly black and white colour, minimal use of other colours is ok
Should not have
• many colours, various fonts

```html
<!DOCTYPE html>
<html lang="en">
<head>
<meta charset="utf-8">
<title>TR Hair Studio – Business Card</title>
<link rel="stylesheet" href="https://fonts.googleapis.com/css2?family=Open+Sans:wght@400;600;700&display=swap">
<style>
  :root {
    --ink-deep: #1a1a1a;
    --ink-dark: #111111;
    --paper: #ffffff;
    --accent: #22bdee;
    --font-body: "Open Sans", Arial, sans-serif;
  }
  html, body {
    margin: 0;
    padding: 0;
    width: 1200px;
    height: 417px;
    overflow: hidden;
    background: var(--ink-deep);
  }
  .card {
    position: relative;
    width: 1200px;
    height: 417px;
    overflow: hidden;
    font-family: var(--font-body);
    color: var(--paper);
  }
  .card-backdrop {
    position: absolute;
    inset: 0;
  }
  .brand-name {
    position: absolute;
    margin: 0;
    font-weight: 700;
    color: var(--paper);
    white-space: nowrap;
    line-height: 1;
  }
  .brand-name--front {
    left: 0;
    width: 640px;
    top: 98px;
    text-align: center;
    font-size: 48px;
    letter-spacing: 1px;
  }
  .brand-name--band {
    left: 880px;
    width: 310px;
    top: 180px;
    text-align: center;
    font-size: 31px;
  }
  .appointment {
    position: absolute;
    left: 23px;
    top: 198px;
    width: 554px;
    height: 196px;
  }
  .appointment-title {
    margin: 0;
    position: absolute;
    left: 12px;
    width: 554px;
    top: 10px;
    text-align: center;
    font-size: 27px;
    font-weight: 700;
    line-height: 1.2;
    text-decoration: underline;
    text-underline-offset: 4px;
    text-decoration-thickness: 2px;
  }
  .appointment-field {
    position: absolute;
    display: flex;
    align-items: flex-end;
    font-size: 27px;
    font-weight: 600;
    line-height: 1.2;
  }
  .appointment-field--date { top: 58px; left: 35px; }
  .appointment-field--time { top: 117px; left: 36px; }
  .field-line {
    display: inline-block;
    height: 2px;
    background: var(--paper);
    margin-left: 4px;
    margin-bottom: 6px;
  }
  .appointment-field--date .field-line { width: 415px; }
  .appointment-field--time .field-line { width: 413px; }
  .contact-list {
    position: absolute;
    list-style: none;
    margin: 0;
    padding: 0;
  }
  .contact-list li {
    position: absolute;
    left: 0;
    display: flex;
    align-items: center;
    white-space: nowrap;
    line-height: 1.2;
  }
  .social-list { left: 644px; top: 0; }
  .social-list li { font-size: 18px; }
  .social-list .handle-primary { top: 38px; }
  .social-list .handle-secondary { top: 72px; }
  .social-dot {
    width: 10px;
    height: 10px;
    border-radius: 50%;
    background: var(--paper);
    border: 4px solid var(--ink-dark);
    margin-right: 6px;
  }
  .details-list { left: 856px; top: 0; }
  .details-list li { font-size: 18px; }
  .details-list .phone { top: 274px; }
  .details-list .address { top: 308px; font-size: 12px; letter-spacing: -0.3px; }
  .details-list .website { top: 335px; }
  .detail-icon {
    width: 14px;
    height: 16px;
    margin-right: 14px;
    flex: none;
  }
</style>
</head>
<body>
<main class="card">
  <svg class="card-backdrop" width="1200" height="417" viewBox="0 0 1200 417" aria-hidden="true">
    <defs>
      <radialGradient id="baseGlow" cx="0.25" cy="0.1" r="0.9">
        <stop offset="0" stop-color="#2e2e2e"/>
        <stop offset="1" stop-color="#1b1b1b"/>
      </radialGradient>
      <linearGradient id="sidePanel" x1="0" y1="0" x2="1" y2="1">
        <stop offset="0" stop-color="#2c2c2c"/>
        <stop offset="1" stop-color="#1f1f1f"/>
      </linearGradient>
      <linearGradient id="apptPanel" x1="0" y1="0" x2="0" y2="1">
        <stop offset="0" stop-color="#222"/>
        <stop offset="1" stop-color="#2f2f2f"/>
      </linearGradient>
      <filter id="edgeShadow" x="-10%" y="-10%" width="120%" height="120%">
        <feDropShadow dx="-4" dy="0" stdDeviation="5" flood-color="#000" flood-opacity="0.7"/>
      </filter>
    </defs>
    <rect width="1200" height="417" fill="url(#baseGlow)"/>
    <polygon points="1032,0 1200,0 1200,417 696,417" fill="url(#sidePanel)" filter="url(#edgeShadow)"/>
    <polygon points="1032,0 1200,0 1200,70" fill="#262626"/>
    <rect x="23" y="198" width="554" height="196" fill="url(#apptPanel)"/>
    <polygon points="824,242 1200,242 1200,153 928,153" fill="#22bdee"/>
  </svg>

  <p class="brand-name brand-name--front">TR Hair Studio</p>

  <section class="appointment">
    <h2 class="appointment-title">Your next appointment :</h2>
    <div class="appointment-field appointment-field--date">Date :<span class="field-line"></span></div>
    <div class="appointment-field appointment-field--time">Time :<span class="field-line"></span></div>
  </section>

  <ul class="contact-list social-list">
    <li class="handle-primary"><span class="social-dot"></span>: @TR_HairStudio</li>
    <li class="handle-secondary"><span class="social-dot"></span>: tr.hairstudio</li>
  </ul>

  <p class="brand-name brand-name--band">TR Hair Studio</p>

  <ul class="contact-list details-list">
    <li class="phone">
      <svg class="detail-icon" viewBox="0 0 14 16" aria-hidden="true">
        <rect x="1" y="0" width="12" height="16" rx="1.5" fill="#fff"/>
        <rect x="4" y="2" width="6" height="11" fill="#222"/>
      </svg>phone : 555 614-2870
    </li>
    <li class="address">
      <svg class="detail-icon" viewBox="0 0 14 16" aria-hidden="true">
        <rect x="0" y="1" width="14" height="14" rx="1" fill="#fff"/>
        <rect x="2" y="3" width="10" height="8" fill="#222"/>
      </svg>address : 2751 Birchfield Rd.E. Maplecrest, ON L7P3K2
    </li>
    <li class="website">
      <svg class="detail-icon" viewBox="0 0 14 16" aria-hidden="true">
        <rect x="0" y="1" width="14" height="14" rx="1" fill="#fff"/>
        <circle cx="7" cy="8" r="5" fill="none" stroke="#222" stroke-width="1.2"/>
        <path d="M2 8h10M7 3v10M4 5.5h6M4 10.5h6" stroke="#222" stroke-width="1"/>
      </svg>website : trhairexample.ca
    </li>
  </ul>
</main>
</body>
</html>
```